Lanternfield Billboard - Financial Services Company (Investments, Tax Planning and Insurance)

Our new office has a billboard directly above the office building. We'd like something eye-catching with a strong Call to Action, with the main part of the billboard being under 7 words if possible. We'd like you to include a way to get ahold of us (either our website lanternfieldllc.example or our phone number 302-418-2967. You may also include in small font something to indicate that we've been serving the area since 1980 (the DE area, the tri-state area, the Copperleaf Basin, etc.)

We offer financial planning, tax planning, and insurance, and we help our clients to focus on their goals and happiness by providing everything they need for lifelong wealth under one roof.

Our logos are attached, we use a triangle logo with green and gray. We use the tagline "Your wealth, well planned" but this does not need to be included.

Potential ideas we have seen from other financial companies-
- the concept that the driver spends more time looking at billboards than planning for their retirement
-something along the lines of "everything you need for your finances is in this building right here" planning, investments, taxes, insurance"
-don't spend your time worrying about retirement, let us help you plan for it
-are you working for your money, or is it working for you?
- retirement takes planning, we're here to help
- ready to retire? talk to us
- need investment advice?
- need help investing?
- crossing your fingers isn't a retirement plan. we can help.
- retiring soon? you need help.

Those are just general ideas, please feel free to be creative.

brand colors:
#00b585
#00b185
#000000
#ffffff
#6d6f75
#6d6f75
#6f7074
#021712
#052e24

```html
<!DOCTYPE html>
<html lang="en">
<head>
<meta charset="utf-8">
<title>Lanternfield Billboard</title>
<link href="https://fonts.googleapis.com/css2?family=Montserrat:wght@500;600;800&display=swap" rel="stylesheet">
<style>
  :root {
    --green: #00a865;
    --green-brand: #00b585;
    --gray: #6d6f75;
    --gray-dark: #58595c;
    --white: #ffffff;
    --mint-light: #f7fbf8;
    --mint: #d6efe6;
    --stage: #eceeef;
  }
  html, body {
    margin: 0;
    padding: 0;
    width: 1200px;
    height: 900px;
    overflow: hidden;
    background: var(--stage);
    font-family: "Montserrat", Arial, sans-serif;
  }
  .billboard {
    position: absolute;
    left: 0;
    top: 192px;
    width: 1200px;
    height: 515px;
    overflow: hidden;
    background: linear-gradient(100deg, var(--mint-light) 0%, #eaf6f1 45%, var(--mint) 100%);
  }
  .billboard-shapes {
    position: absolute;
    inset: 0;
  }
  .brand {
    position: absolute;
    left: 104px;
    top: 62px;
  }
  .brand-row {
    display: flex;
    align-items: center;
    gap: 14px;
  }
  .brand-mark {
    width: 30px;
    height: 30px;
    background: var(--green);
  }
  .brand-name {
    font-weight: 600;
    font-size: 56px;
    line-height: 1;
    color: var(--green);
    letter-spacing: -0.5px;
  }
  .brand-tagline {
    margin: 10px 0 0 146px;
    font-weight: 500;
    font-size: 11px;
    letter-spacing: 4.2px;
    color: var(--gray);
    text-transform: uppercase;
    white-space: nowrap;
  }
  .headline {
    position: absolute;
    left: 54px;
    top: 190px;
    margin: 0;
    font-weight: 800;
    font-size: 66px;
    line-height: 65px;
    text-transform: uppercase;
    color: var(--green);
    letter-spacing: -0.5px;
  }
  .headline .muted { color: var(--gray-dark); }
  .contact {
    position: absolute;
    left: 54px;
    top: 428px;
    height: 87px;
    display: flex;
    align-items: center;
    gap: 30px;
    color: var(--white);
    font-weight: 800;
  }
  .contact-label {
    font-size: 30px;
    letter-spacing: 1.5px;
  }
  .contact-phone {
    display: flex;
    align-items: center;
    gap: 10px;
    font-size: 38px;
    letter-spacing: -0.5px;
  }
  .phone-icon { width: 44px; height: 44px; }
  .photo {
    position: absolute;
    left: 780px;
    top: 20px;
    width: 420px;
    height: 495px;
    background: linear-gradient(160deg, #e6ddd2 0%, #d9b8a0 40%, #2c4f8c 75%, #bcc4cf 100%);
  }
</style>
</head>
<body>
  <section class="billboard">
    <svg class="billboard-shapes" width="1200" height="515" viewBox="0 0 1200 515" aria-hidden="true">
      <polygon class="accent-band" points="925,0 1065,0 1200,280 1200,515 703,515" fill="var(--green)"/>
      <polygon class="contact-bar" points="0,428 703,428 660,515 0,515" fill="var(--gray)"/>
    </svg>

    <div class="photo" role="img" aria-label="Photo of a smiling retired couple embracing"></div>

    <div class="brand">
      <div class="brand-row">
        <span class="brand-mark"></span>
        <span class="brand-name">Lanternfield</span>
      </div>
      <div class="brand-tagline">Your wealth, well planned</div>
    </div>

    <h1 class="headline">
      Retirement <span class="muted">takes</span><br>
      <span class="muted">planning,</span> we're<br>
      here to help
    </h1>

    <div class="contact">
      <span class="contact-label">CALL US</span>
      <span class="contact-phone">
        <svg class="phone-icon" viewBox="0 0 44 44" aria-hidden="true">
          <circle cx="22" cy="22" r="22" fill="var(--white)"/>
          <path d="M15 11c1-1 2.5-1 3.3 0l2.6 3.6c.7 1 .5 2.3-.4 3l-1.6 1.3c1.2 2.6 3.2 4.6 5.8 5.8l1.3-1.6c.7-.9 2-1.1 3-.4l3.6 2.6c1 .8 1 2.3 0 3.3l-1.8 1.8c-1.4 1.4-3.6 1.7-5.4.8-5.4-2.6-9.8-7-12.4-12.4-.9-1.8-.6-4 .8-5.4z" fill="var(--gray)"/>
        </svg>
        302-418-2967
      </span>
    </div>
  </section>
</body>
</html>
```